SnackHarbor!!! A Vending Machine Business Looking for an attractive website.

We are a vending machine business in Northern Michigan. We have changed our name and have rebranded our company. We would like an attractive website that shares who we are, what services we provide, the products we offer in our machines, along with a form businesses can fill out to see if they are a good fit for our company. I would like to have a Home Page, About SnackHarbor, Why Choose SnackHarbor?, Products & Services, Contact Us (With a Login Option), and a page with a questionnaire for thos interested in getting a FREE Vending Machine.

Target Market(s)

Businesses, Campgrounds, Schools, and many more in Northern Michigan

Industry/Entity Type

Vending Machines

Number of Pages Required

5+ page

Requirements
Must have
• An inviting and enticing Home Page. I want to get my potential clients engaged in our website.
Nice to have
• Possibly background photos from Northern Michigan
Should not have
• A corporate feel. I do not want a boring website.

```html
<!DOCTYPE html>
<html lang="en">
<head>
<meta charset="utf-8">
<title>SnackHarbor – Crave. Vend. Repeat.</title>
<link rel="stylesheet" href="https://fonts.googleapis.com/css2?family=Archivo:wght@300;400;500;700;800;900&display=swap">
<style>
:root{
  --green:#2b5a27;
  --purple:#3a2570;
  --purple-deep:#2a1a55;
  --ink:#111;
  --text:#2a2a2a;
  --white:#fff;
  --gold:#f2b51c;
  --footer:#000;
}
*{margin:0;padding:0;box-sizing:border-box}
html,body{width:1200px;height:4409px;overflow:hidden}
body{font-family:"Archivo",sans-serif;color:var(--text);background:var(--white);position:relative}
.abs{position:absolute}
.btn{position:absolute;display:flex;align-items:center;justify-content:center;background:var(--green);color:var(--white);font-size:13px;font-weight:500;text-decoration:none}
/* header */
.top-bar{position:absolute;left:0;top:0;width:1200px;height:7px;background:var(--green)}
.site-header{position:absolute;left:0;top:7px;width:1200px;height:118px;background:var(--white)}
.brand{position:absolute;font-weight:900;color:var(--purple);letter-spacing:-0.5px}
.nav{position:absolute;left:375px;top:55px;display:flex;gap:20px;font-size:13px;color:#333}
/* hero */
.hero{position:absolute;left:0;top:125px;width:1200px;height:630px;overflow:hidden}
.hero-photo{position:absolute;inset:0;background:
  linear-gradient(90deg,rgba(38,44,66,.42) 0%,rgba(38,44,66,.18) 38%,rgba(38,44,66,0) 60%),
  linear-gradient(180deg,#d3d5d8 0%,#b4b7bc 38%,#9ea2a8 52%,#d9dadd 68%,#f1f1f2 100%)}
.hero-title{position:absolute;left:108px;top:228px;font-size:33px;font-weight:800;color:var(--white);text-shadow:0 2px 4px rgba(0,0,0,.35)}
.hero-sub{position:absolute;left:110px;top:284px;font-size:19px;font-weight:700;color:var(--purple-deep)}
/* about */
.section-title{position:absolute;font-weight:800;color:var(--ink)}
.about-text{position:absolute;left:113px;top:880px;width:448px;font-size:14px;line-height:30px;color:#222}
/* why */
.why{position:absolute;left:0;top:1250px;width:1200px;height:558px;background:linear-gradient(180deg,rgba(58,37,112,.92),rgba(52,33,100,.95)),linear-gradient(90deg,#553d7d,#3a2570)}
.why h2{position:absolute;left:0;width:1200px;top:68px;text-align:center;font-size:40px;font-weight:900;color:var(--white)}
.why-col{position:absolute;top:180px;width:210px;text-align:center;color:var(--white)}
.why-col svg{display:block;margin:0 auto}
.why-col h3{font-size:15px;font-weight:700;line-height:22px;margin-top:18px;min-height:44px;display:flex;align-items:center;justify-content:center}
.why-col p{font-size:11.5px;line-height:23px;margin-top:6px}
.why-arrow{position:absolute;top:450px}
/* services */
.tabs{position:absolute;left:173px;top:1970px;width:854px;height:101px;display:flex;border:1px solid #ddd}
.tab{flex:1;border-right:1px solid #ddd;display:flex;flex-direction:column;align-items:center;justify-content:center;gap:10px;font-size:12px;color:#333}
.tab:last-child{border-right:none}
.tab.active{background:var(--green);color:var(--white)}
.svc-text{position:absolute;left:644px;top:2212px;width:440px;font-size:14px;line-height:30px;color:#333}
/* questionnaire */
.quiz{position:absolute;left:0;top:2535px;width:1200px;height:396px;background:linear-gradient(90deg,rgba(43,90,39,.93),rgba(38,84,35,.9)),linear-gradient(180deg,#5b7a52,#3d6436)}
.quiz h2{position:absolute;width:1200px;top:88px;text-align:center;font-size:40px;font-weight:800;color:var(--white)}
.quiz p{position:absolute;left:290px;width:620px;top:168px;text-align:center;font-size:14px;line-height:30px;color:var(--white)}
.quiz .btn{left:530px;top:278px;width:124px;height:41px;background:var(--white);color:#222}
/* products */
.card{position:absolute;top:3099px;height:441px;background:var(--white);box-shadow:0 2px 10px rgba(0,0,0,.12)}
.card-img{position:absolute;left:10px;top:13px;right:10px;height:329px}
.card h4{position:absolute;left:20px;top:356px;font-size:17px;font-weight:700;color:#111}
.card .price{position:absolute;left:28px;top:391px;font-size:13px;color:#333}
.card .stars{position:absolute;right:22px;top:391px;font-size:11px;color:var(--gold);letter-spacing:1px}
.card-icons{position:absolute;right:18px;top:28px;display:flex;flex-direction:column;gap:8px}
.card-icons span{width:26px;height:26px;border-radius:50%;background:var(--white);display:flex;align-items:center;justify-content:center}
/* footer */
.footer{position:absolute;left:0;top:3826px;width:1200px;height:583px;background:var(--footer);color:var(--white)}
.cta-title{position:absolute;left:125px;top:62px;font-size:36px;font-weight:300;line-height:48px}
.cta-text{position:absolute;left:651px;top:72px;width:440px;font-size:14px;line-height:30px}
.f-col{position:absolute;top:255px}
.f-col h5{font-size:19px;font-weight:700;margin-bottom:30px}
.f-col li{list-style:none;font-size:13px;line-height:33.5px}
.contact-row{display:flex;align-items:center;gap:18px;font-size:13px;height:66px}
.social{position:absolute;top:350px;display:flex;gap:6px;left:115px}
.social span{width:27px;height:27px;border-radius:3px}
.f-rule{position:absolute;left:111px;top:536px;width:978px;height:1px;background:#888}
.copy{position:absolute;top:556px;width:1200px;text-align:center;font-size:11px}
</style>
</head>
<body>

<div class="top-bar"></div>
<header class="site-header">
  <div class="brand" style="left:108px;top:30px;font-size:34px">SnackHarbor</div>
  <nav class="nav">
    <span>Home</span><span>About SnackHarbor</span><span>Why Choose SnackHarbor?</span><span>Products</span><span>Services</span>
  </nav>
  <svg class="abs" style="left:919px;top:54px" width="18" height="20" viewBox="0 0 18 20" fill="none" stroke="#333" stroke-width="1.5"><circle cx="9" cy="6" r="4"/><path d="M2 19c0-4 3-6 7-6s7 2 7 6z"/></svg>
  <a class="btn" style="left:964px;top:41px;width:125px;height:48px">Contact Us</a>
</header>

<section class="hero">
  <div class="hero-photo" role="img" aria-label="Row of modern vending machines in a bright lobby with a polished floor"></div>
  <div class="brand" style="left:108px;top:118px;font-size:64px;color:var(--purple-deep)">SnackHarbor</div>
  <div class="hero-title">Crave. Vend. Repeat.</div>
  <div class="hero-sub">Elevating Snacking, One Vend at a Time</div>
  <a class="btn" style="left:111px;top:334px;width:118px;height:46px">Get Started</a>
  <svg class="abs" style="left:0;top:520px" width="1200" height="110" viewBox="0 0 1200 110" preserveAspectRatio="none">
    <path d="M0 55 C180 -10 260 5 380 50 C520 105 640 55 760 30 C880 5 1000 20 1200 60 L1200 110 L0 110Z" fill="var(--purple-deep)"/>
    <path d="M0 65 C180 5 260 20 380 62 C520 112 640 68 760 44 C880 22 1000 35 1200 72 L1200 110 L0 110Z" fill="var(--green)"/>
    <path d="M0 78 C180 22 260 36 380 76 C520 120 640 84 760 60 C880 38 1000 52 1200 86 L1200 110 L0 110Z" fill="var(--white)"/>
  </svg>
</section>

<h2 class="section-title" style="left:113px;top:812px;font-size:41px">About SnackHarbor</h2>
<p class="about-text">At SnackHarbor, we don't just vend snacks—we curate cravings. Our customized vending solutions bring flavor, convenience, and community to Northern Michigan. Whether you're reaching for a mid-morning snack, a refreshing beverage, or a satisfying breakfast burrito, SnackHarbor delivers delight with every bite.</p>
<a class="btn" style="left:115px;top:1082px;width:123px;height:43px">Read More</a>
<div class="abs" role="img" aria-label="Stocked snack vending machine" style="left:745px;top:805px;width:294px;height:359px;background:linear-gradient(135deg,#e8e9eb,#c4c6ca 50%,#d9b24a 75%,#9a9da2)"></div>

<section class="why">
  <h2>Why Choose SnackHarbor?</h2>
  <div class="why-col" style="left:119px">
    <svg width="44" height="44" viewBox="0 0 44 44" fill="none" stroke="#fff" stroke-width="2"><path d="M28 20s-8-5-8-10a4 4 0 0 1 8-1 4 4 0 0 1 8 1c0 5-8 10-8 10z"/><path d="M4 34h10l8 4 12-6M4 26h8l8 3"/></svg>
    <h3>Local Love</h3>
    <p>We celebrate the heart of Michigan by partnering with local legends. Say hello to Pine Ridge Jerky and Bayshore Kettle Chips—our hometown heroes.</p>
  </div>
  <div class="why-col" style="left:369px">
    <svg width="44" height="44" viewBox="0 0 44 44" fill="none" stroke="#fff" stroke-width="2"><circle cx="22" cy="22" r="17"/><path d="M14 25c3 5 13 5 16 0M16 17h.1M28 17h.1"/></svg>
    <h3>Unleash Your<br>Cravings</h3>
    <p>SnackHarbor isn't bound by corporate ties. We're the rebels of the vending world. Craving a bag of crispy, kettle-cooked chips? Done..</p>
  </div>
  <div class="why-col" style="left:611px">
    <svg width="44" height="44" viewBox="0 0 44 44" fill="none" stroke="#fff" stroke-width="2"><path d="M22 4l5 4 6-1 1 6 5 4-3 5 3 5-5 4-1 6-6-1-5 4-5-4-6 1-1-6-5-4 3-5-3-5 5-4 1-6 6 1z"/><path d="M15 22l5 5 9-10"/></svg>
    <h3>Quality Meets<br>Convenience</h3>
    <p>Imagine this: You're mid-meeting, and your stomach growls. Fear not! SnackHarbor's machines offer top-notch snacks and beverages.</p>
  </div>
  <div class="why-col" style="left:859px">
    <svg width="44" height="44" viewBox="0 0 44 44" fill="none" stroke="#fff" stroke-width="2"><path d="M22 4l14 5v11c0 10-6 16-14 20C14 36 8 30 8 20V9z"/><path d="M22 14c-4 5-5 8-5 10a5 5 0 0 0 10 0c0-2-1-5-5-10z"/></svg>
    <h3>Pandemic-Proof &amp;<br>Recession-Ready</h3>
    <p>Life throws curveballs, but SnackHarbor stands strong. Our vending machines are the unsung heroes of resilience. Rain or shine, they're there, serving up joy.</p>
  </div>
  <svg class="why-arrow" style="left:214px" width="22" height="14" viewBox="0 0 22 14" fill="none" stroke="#fff" stroke-width="1.6"><path d="M1 7h19M14 1l6 6-6 6"/></svg>
  <svg class="why-arrow" style="left:463px;top:473px" width="22" height="14" viewBox="0 0 22 14" fill="none" stroke="#fff" stroke-width="1.6"><path d="M1 7h19M14 1l6 6-6 6"/></svg>
  <svg class="why-arrow" style="left:706px;top:473px" width="22" height="14" viewBox="0 0 22 14" fill="none" stroke="#fff" stroke-width="1.6"><path d="M1 7h19M14 1l6 6-6 6"/></svg>
  <svg class="why-arrow" style="left:953px;top:473px" width="22" height="14" viewBox="0 0 22 14" fill="none" stroke="#fff" stroke-width="1.6"><path d="M1 7h19M14 1l6 6-6 6"/></svg>
</section>

<h2 class="section-title" style="left:0;width:1185px;text-align:center;top:1884px;font-size:41px">Our Services</h2>
<div class="tabs">
  <div class="tab active"><svg width="30" height="40" viewBox="0 0 30 40" fill="none" stroke="currentColor" stroke-width="1.5"><rect x="2" y="2" width="26" height="36" rx="2"/><path d="M6 8h18M6 14h18M6 20h18M6 26h18M8 32h14"/></svg>Food &amp; Snacks</div>
  <div class="tab"><svg width="30" height="40" viewBox="0 0 30 40" fill="none" stroke="currentColor" stroke-width="1.5"><rect x="2" y="2" width="26" height="36" rx="2"/><rect x="6" y="6" width="14" height="24"/><path d="M24 10v6M8 34h14"/></svg>Drinks &amp; Coffee</div>
  <div class="tab"><svg width="30" height="40" viewBox="0 0 30 40" fill="none" stroke="currentColor" stroke-width="1.5"><circle cx="15" cy="12" r="9"/><path d="M9 21h12v15H9zM13 28h4"/></svg>Gumball &amp; Candy</div>
  <div class="tab"><svg width="30" height="40" viewBox="0 0 30 40" fill="none" stroke="currentColor" stroke-width="1.5"><rect x="2" y="2" width="26" height="36" rx="2"/><path d="M6 8h18v16H6zM6 30h18"/></svg>Cold &amp; Frozen</div>
  <div class="tab" style="color:#444"><svg width="30" height="40" viewBox="0 0 30 40" fill="none" stroke="#999" stroke-width="1.5"><rect x="5" y="2" width="20" height="30" rx="2"/><path d="M9 7h12v12H9zM10 36h10"/></svg>Custom Machines</div>
</div>
<div class="abs" role="img" aria-label="Black glass-front snack vending machine" style="left:337px;top:2131px;width:218px;height:351px;background:linear-gradient(180deg,#2e2e31,#4a4155 40%,#3a3a3d 80%,#2b2b2d)"></div>
<h3 class="abs" style="left:645px;top:2158px;font-size:24px;font-weight:700;color:#111">Food &amp; Snacks</h3>
<p class="svc-text">Lorem ipsum dolor sit amet, consectetur adipiscing elit, sed do eiusmod tempor incididunt ut labore et dolore magna aliqua. Ut enim ad minim veniam, quis nostrud exercitation ullamco laboris nisi ut aliquip ex ea commodo consequat. Duis aute irure dolor in reprehenderit in voluptate velit esse cillum dolore eu fugiat nulla pariatur.</p>
<a class="btn" style="left:644px;top:2397px;width:123px;height:39px">Read More</a>

<section class="quiz" role="img" aria-label="Shelves of packaged snacks behind a green overlay">
  <h2>Get a questionnaire</h2>
  <p>Lorem ipsum dolor sit amet, consectetur adipiscing elit, sed do eiusmod tempor incididunt ut labore et dolore magna aliqua. Ut enim ad minim veniam, quis nostrud exercitation ullamco laboris nisi ut aliquip ex ea commodo consequat.</p>
  <a class="btn">Click Here</a>
</section>

<h2 class="section-title" style="left:0;width:1205px;text-align:center;top:3007px;font-size:41px">Our Products</h2>

<div class="card" style="left:111px;width:308px">
  <div class="card-img" role="img" aria-label="Lit beverage vending machine beside a stone wall" style="background:linear-gradient(135deg,#3b2e26,#22405f 45%,#1c2a3a 80%,#2a2622)"></div>
  <div class="card-icons">
    <span><svg width="14" height="14" viewBox="0 0 16 16" fill="none" stroke="#333" stroke-width="1.3"><path d="M8 14s-6-4-6-8a3 3 0 0 1 6-1 3 3 0 0 1 6 1c0 4-6 8-6 8z"/></svg></span>
    <span><svg width="14" height="14" viewBox="0 0 16 16" fill="none" stroke="#333" stroke-width="1.3"><ellipse cx="8" cy="8" rx="7" ry="4"/><circle cx="8" cy="8" r="1.8"/></svg></span>
    <span><svg width="14" height="14" viewBox="0 0 16 16" fill="none" stroke="#333" stroke-width="1.3"><path d="M1 2h3l2 8h8l2-6H5M7 14h.1M13 14h.1"/></svg></span>
  </div>
  <h4>Beverages Vending Machines</h4><span class="price">$150.00</span><span class="stars">★★★★★</span>
</div>
<div class="card" style="left:442px;width:308px">
  <div class="card-img" role="img" aria-label="Snack vending machine with stocked spiral shelves" style="background:linear-gradient(135deg,#3a3a3c,#8f9296 40%,#a56c4c 75%,#4a4a4c)"></div>
  <div class="card-icons">
    <span><svg width="14" height="14" viewBox="0 0 16 16" fill="none" stroke="#333" stroke-width="1.3"><path d="M8 14s-6-4-6-8a3 3 0 0 1 6-1 3 3 0 0 1 6 1c0 4-6 8-6 8z"/></svg></span>
    <span><svg width="14" height="14" viewBox="0 0 16 16" fill="none" stroke="#333" stroke-width="1.3"><ellipse cx="8" cy="8" rx="7" ry="4"/><circle cx="8" cy="8" r="1.8"/></svg></span>
    <span><svg width="14" height="14" viewBox="0 0 16 16" fill="none" stroke="#333" stroke-width="1.3"><path d="M1 2h3l2 8h8l2-6H5M7 14h.1M13 14h.1"/></svg></span>
  </div>
  <h4>Snacks Vending Machines</h4><span class="price">$450.00</span><span class="stars">★★★★★</span>
</div>
<div class="card" style="left:774px;width:316px">
  <div class="card-img" role="img" aria-label="Close view of candy bars and chips on vending spirals" style="background:linear-gradient(160deg,#5a3f7a,#b8763a 45%,#2f3f7a 75%,#a8452f)"></div>
  <div class="card-icons">
    <span><svg width="14" height="14" viewBox="0 0 16 16" fill="none" stroke="#333" stroke-width="1.3"><path d="M8 14s-6-4-6-8a3 3 0 0 1 6-1 3 3 0 0 1 6 1c0 4-6 8-6 8z"/></svg></span>
    <span><svg width="14" height="14" viewBox="0 0 16 16" fill="none" stroke="#333" stroke-width="1.3"><ellipse cx="8" cy="8" rx="7" ry="4"/><circle cx="8" cy="8" r="1.8"/></svg></span>
    <span><svg width="14" height="14" viewBox="0 0 16 16" fill="none" stroke="#333" stroke-width="1.3"><path d="M1 2h3l2 8h8l2-6H5M7 14h.1M13 14h.1"/></svg></span>
  </div>
  <h4>Chocolates Vending Machine</h4><span class="price">$350.00</span><span class="stars">★★★★★</span>
</div>
<a class="btn" style="left:540px;top:3569px;width:122px;height:40px">View All</a>

<svg class="abs" style="left:0;top:3700px" width="1200" height="130" viewBox="0 0 1200 130" preserveAspectRatio="none">
  <path d="M0 40 C150 100 300 110 450 60 C600 10 700 0 820 50 C950 100 1080 90 1200 30 L1200 130 L0 130Z" fill="var(--purple-deep)"/>
  <path d="M0 55 C150 112 300 122 450 74 C600 26 700 16 820 64 C950 112 1080 104 1200 46 L1200 130 L0 130Z" fill="var(--white)"/>
  <path d="M0 62 C150 118 300 128 450 82 C600 36 700 26 820 72 C950 118 1080 112 1200 56 L1200 130 L0 130Z" fill="var(--green)"/>
  <path d="M0 74 C150 126 300 134 450 94 C600 52 700 42 820 86 C950 126 1080 122 1200 72 L1200 130 L0 130Z" fill="var(--footer)"/>
</svg>

<footer class="footer">
  <div class="cta-title">Ready to experience the<br>SnackHarbor difference?</div>
  <p class="cta-text">Sign up now and let's connect. Taste the future of snacking firsthand! Contact us today and explore how our vending magic can elevate your space</p>
  <div class="brand" style="left:111px;top:240px;font-size:40px;color:var(--white)">SnackHarbor</div>
  <div class="social"><span style="background:#1877f2"></span><span style="background:#fff"></span><span style="background:#e60023"></span><span style="background:#c13584"></span><span style="background:#ff0000"></span></div>
  <div class="f-col" style="left:430px"><h5>Quick Links</h5><ul><li>Home</li><li>About SnackHarbor</li><li>Why Choose SnackHarbor?</li><li>&nbsp;Products</li><li>Services</li><li>Contact Us</li></ul></div>
  <div class="f-col" style="left:662px"><h5>Contact Info</h5>
    <div class="contact-row" style="height:40px"><svg width="24" height="24" viewBox="0 0 24 24"><rect width="24" height="24" rx="4" fill="#fff"/><path d="M12 5a5 5 0 0 0-5 5c0 4 5 9 5 9s5-5 5-9a5 5 0 0 0-5-5z" fill="#000"/><circle cx="12" cy="10" r="2" fill="#fff"/></svg>Lorem Ipsum,Usa - 437916</div>
    <div class="contact-row"><svg width="24" height="24" viewBox="0 0 24 24"><rect width="24" height="24" rx="4" fill="#fff"/><path d="M7 5l3 1 1 4-2 1c1 2 2 3 4 4l1-2 4 1 1 3c0 1-1 2-2 2C11 19 5 13 5 7c0-1 1-2 2-2z" fill="#000"/></svg>+1 888 888 8888</div>
    <div class="contact-row"><svg width="24" height="24" viewBox="0 0 24 24"><rect width="24" height="24" rx="4" fill="#fff"/><rect x="5" y="7" width="14" height="10" fill="none" stroke="#000" stroke-width="1.5"/><path d="M5 7l7 6 7-6" fill="none" stroke="#000" stroke-width="1.5"/></svg>info@snackharbor</div>
  </div>
  <div class="f-col" style="left:957px"><h5>Help Links</h5><ul><li>Privay Policy</li><li>Terms &amp; Conditions</li></ul></div>
  <div class="f-rule"></div>
  <div class="copy">Copyright © 2024 &nbsp;SnackHarbor. All rights reserved.</div>
</footer>

</body>
</html>
```